Life Coach for Lawyers Business Card Design

Elegant, original, business card design for life coaching service for associate attorneys who work in big law and struggle with stress, overwhelm, and time management. Double sided design.

Target Market(s)

Women associate attorneys who work in big law and struggle with stress, overwhelm, and time management.

Industry/Entity Type

Life Coaching

Contact Information for Business Card

Marissa Pendrell
Life Coach
518.677.3941
calmbriefcounsel.net
marissa@calmbriefcounsel.net
@calmbriefcounsel (Instagram)

Font styles to use
Other font styles liked:
• Silver South font duo. See uploaded files.

Requirements
Must have
• Icons for phone, website, email, and Instagram instead of words. Specific colors used in my logo (171B2B, 421121, FFFFFF)
Nice to have
• Foil. Embossed. Feminine design.
Should not have
• Any colors other than those used in logo. See uploaded files.

```html
<!DOCTYPE html>
<html lang="en">
<head>
<meta charset="utf-8">
<title>Calm Brief Counsel — Business Card</title>
<link rel="stylesheet" href="https://fonts.googleapis.com/css2?family=Bodoni+Moda:wght@400;500&family=Jost:wght@400&family=Sacramento&display=swap">
<style>
  :root {
    --navy: #171B2B;
    --plum: #421121;
    --white: #FFFFFF;
    --edge: #8a8c93;
  }
  * { margin: 0; padding: 0; box-sizing: border-box; }
  html, body {
    width: 934px;
    height: 1200px;
    overflow: hidden;
    background: var(--white);
  }
  .canvas {
    position: relative;
    width: 934px;
    height: 1200px;
  }

  /* Front side */
  .card-front {
    position: absolute;
    left: 0; top: 0;
    width: 934px;
    height: 533px;
    background: var(--navy);
  }
  .brand-seal {
    position: absolute;
    left: 267px; top: 67px;
    width: 400px; height: 400px;
    border: 1.5px solid var(--white);
    border-radius: 50%;
    display: flex;
    align-items: center;
    justify-content: center;
  }
  .brand-name {
    font-family: "Bodoni Moda", serif;
    font-weight: 400;
    font-size: 19px;
    letter-spacing: 0.24em;
    color: var(--white);
    text-transform: uppercase;
    white-space: nowrap;
    margin-right: -0.24em;
  }

  /* Back side */
  .card-back {
    position: absolute;
    left: 0; top: 667px;
    width: 934px;
    height: 533px;
    border: 1px solid var(--edge);
    background: var(--white);
  }
  .person-name {
    position: absolute;
    left: 146px; top: 50px;
    font-family: "Sacramento", cursive;
    font-weight: 400;
    font-size: 104px;
    line-height: 1.2;
    color: var(--plum);
    white-space: nowrap;
  }
  .person-role {
    position: absolute;
    left: 146px; top: 210px;
    font-family: "Bodoni Moda", serif;
    font-weight: 500;
    font-size: 22px;
    letter-spacing: 0.45em;
    color: var(--navy);
    white-space: nowrap;
  }
  .contact-list {
    position: absolute;
    left: 133px; top: 272px;
    list-style: none;
  }
  .contact-item {
    display: flex;
    align-items: center;
    height: 52px;
  }
  .contact-icon {
    width: 37px; height: 37px;
    flex: none;
    margin-right: 14px;
  }
  .contact-text {
    font-family: "Jost", sans-serif;
    font-weight: 400;
    font-size: 27px;
    letter-spacing: 0.27em;
    color: var(--navy);
    white-space: nowrap;
  }
</style>
</head>
<body>
<main class="canvas">

  <section class="card-front" aria-label="Card front">
    <div class="brand-seal">
      <span class="brand-name">Calm Brief Counsel</span>
    </div>
  </section>

  <section class="card-back" aria-label="Card back">
    <h1 class="person-name">Marissa Pendrell</h1>
    <p class="person-role">-LIFE COACH-</p>

    <ul class="contact-list">
      <li class="contact-item">
        <svg class="contact-icon" viewBox="0 0 38 38" aria-hidden="true">
          <circle cx="19" cy="19" r="19" fill="var(--plum)"/>
          <path d="M12.5 10.5c1-.8 2.2-.6 2.8.3l1.8 2.8c.5.8.3 1.8-.4 2.4l-1.2 1c.9 2 2.5 3.7 4.5 4.6l1-1.2c.6-.7 1.6-.9 2.4-.4l2.8 1.8c.9.6 1.1 1.8.3 2.8l-1.1 1.3c-1 1.1-2.6 1.5-4 .9-4.6-1.8-8.2-5.4-10-10-.6-1.4-.2-3 .9-4z" fill="var(--white)"/>
        </svg>
        <span class="contact-text">518.677.3941</span>
      </li>
      <li class="contact-item">
        <svg class="contact-icon" viewBox="0 0 38 38" aria-hidden="true">
          <circle cx="19" cy="19" r="19" fill="var(--plum)"/>
          <g fill="none" stroke="var(--white)" stroke-width="1.4">
            <circle cx="19" cy="19" r="9"/>
            <ellipse cx="19" cy="19" rx="4" ry="9"/>
            <line x1="10" y1="19" x2="28" y2="19"/>
            <line x1="11.5" y1="14.5" x2="26.5" y2="14.5"/>
            <line x1="11.5" y1="23.5" x2="26.5" y2="23.5"/>
          </g>
        </svg>
        <span class="contact-text">calmbriefcounsel.net</span>
      </li>
      <li class="contact-item">
        <svg class="contact-icon" viewBox="0 0 38 38" aria-hidden="true">
          <circle cx="19" cy="19" r="19" fill="var(--plum)"/>
          <g fill="none" stroke="var(--white)" stroke-width="1.6" stroke-linejoin="round">
            <rect x="9.5" y="12.5" width="19" height="13" rx="1"/>
            <polyline points="9.5,13 19,20.5 28.5,13"/>
          </g>
        </svg>
        <span class="contact-text">marissa@calmbriefcounsel.net</span>
      </li>
      <li class="contact-item">
        <svg class="contact-icon" viewBox="0 0 38 38" aria-hidden="true">
          <circle cx="19" cy="19" r="19" fill="var(--plum)"/>
          <g fill="none" stroke="var(--white)" stroke-width="1.6" stroke-linecap="round">
            <circle cx="19" cy="15" r="4"/>
            <path d="M11.5 27c.8-4 3.9-6.5 7.5-6.5s6.7 2.5 7.5 6.5"/>
          </g>
        </svg>
        <span class="contact-text">@calmbriefcounsel</span>
      </li>
    </ul>
  </section>

</main>
</body>
</html>
```